!st birthday celebration

Im looking for a celebration type of flyer for our first birthday. something colorful and eye catching but with a vintage feel to it. we are a vintage shop with a friendly atmosphere and always have music playing. I have attached a draft copy i have been working on so far. Thanks

Industry/Entity Type

Shop

```html
<!DOCTYPE html>
<html lang="en">
<head>
<meta charset="utf-8">
<title>Fern Vintage – 1st Birthday Flyer</title>
<link href="https://fonts.googleapis.com/css2?family=Lato:wght@400;900&family=Cinzel:wght@700&family=Bebas+Neue&family=Russo+One&display=swap" rel="stylesheet">
<style>
  :root{
    --red:#e4161c;
    --red-deep:#c70f15;
    --yellow:#ffc20e;
    --gold:#c9962c;
    --gold-soft:#e8c878;
    --ink:#2b2b2b;
    --white:#ffffff;
    --ray:#ececec;
    --page:#dcdcdc;
  }
  *{margin:0;padding:0;box-sizing:border-box}
  html,body{width:904px;height:1200px;overflow:hidden;background:var(--page)}
  .flyer{
    position:relative;width:904px;height:1200px;overflow:hidden;
    background:
      repeating-conic-gradient(from 0deg at 450px 420px, var(--white) 0deg 9deg, var(--ray) 9deg 18deg);
  }
  .flourish{
    position:absolute;left:120px;top:20px;width:700px;height:330px;
    background:radial-gradient(ellipse at 45% 45%, rgba(201,150,44,.85) 0%, rgba(232,200,120,.55) 40%, rgba(232,200,120,0) 72%);
  }
  .decor{position:absolute}
  .decor--top-left{left:0;top:0}
  .decor--top-right{right:0;top:0}
  .decor--bottom-left{left:0;bottom:0;z-index:3}

  .greeting{
    position:absolute;left:202px;top:100px;width:467px;height:147px;
    background:var(--yellow);border:7px solid var(--white);border-radius:26px;
    box-shadow:0 0 0 2px rgba(0,0,0,.05);
    text-align:center;font-family:"Lato",sans-serif;white-space:nowrap;overflow:hidden;
  }
  .greeting__line{display:block;font-size:33px;line-height:40px;color:var(--ink);margin-top:18px;letter-spacing:.5px}
  .greeting__name{display:block;font-size:44px;line-height:52px;font-weight:900;color:var(--red);margin-top:4px}

  .invite{
    position:absolute;left:0;top:370px;width:904px;height:157px;
    background:linear-gradient(var(--red) 0%, var(--red-deep) 100%);
    color:var(--white);text-align:center;
    font-family:"Cinzel",serif;font-size:40px;line-height:58px;padding-top:22px;letter-spacing:1px;
  }

  .activities{
    position:absolute;top:552px;list-style:none;
    font-family:"Bebas Neue",sans-serif;font-size:37px;color:var(--ink);white-space:nowrap;
  }
  .activities--left{left:74px}
  .activities--right{left:580px}
  .activities li{height:51px;display:flex;align-items:center}
  .activities li::before{
    content:"";width:14px;height:14px;border-radius:50%;
    background:var(--white);border:4px solid var(--red);
    box-shadow:0 0 0 3px var(--yellow);margin-right:8px;flex:none;
  }

  .when{
    position:absolute;right:38px;top:820px;text-align:right;white-space:nowrap;
    font-family:"Bebas Neue",sans-serif;font-size:68px;line-height:78px;color:var(--ink);
  }
  .when__label{color:var(--red)}

  .contact{
    position:absolute;left:0;top:1003px;width:904px;height:197px;
    background:linear-gradient(var(--red) 0%, var(--red-deep) 100%);
    color:var(--white);font-family:"Russo One",sans-serif;font-size:20px;line-height:31px;
    text-align:center;padding-top:64px;padding-left:80px;letter-spacing:.5px;
  }
</style>
</head>
<body>
<main class="flyer">
  <div class="flourish" role="img" aria-label="Gold swirl flourish ornament"></div>

  <svg class="decor decor--top-left" width="230" height="320" viewBox="0 0 230 320" aria-hidden="true">
    <circle cx="60" cy="70" r="105" fill="var(--red)"/>
    <circle cx="85" cy="110" r="80" fill="var(--yellow)"/>
    <circle cx="110" cy="195" r="98" fill="var(--white)"/>
    <circle cx="110" cy="195" r="88" fill="var(--red)"/>
    <circle cx="95" cy="235" r="76" fill="var(--yellow)"/>
  </svg>

  <svg class="decor decor--top-right" width="160" height="330" viewBox="0 0 160 330" aria-hidden="true">
    <circle cx="80" cy="-10" r="75" fill="var(--yellow)"/>
    <circle cx="100" cy="20" r="60" fill="var(--red)"/>
    <circle cx="140" cy="185" r="95" fill="var(--red)"/>
    <circle cx="148" cy="185" r="80" fill="var(--white)"/>
    <circle cx="150" cy="185" r="72" fill="var(--yellow)"/>
  </svg>

  <div class="greeting">
    <span class="greeting__line">HAPPY 1ST BIRTHDAY</span>
    <span class="greeting__name">FERN VINTAGE!</span>
  </div>

  <h1 class="invite">You are invited to help<br>celebrate in the festivities!</h1>

  <ul class="activities activities--left">
    <li>Pop up market stalls,</li>
    <li>Best dressed vintage outfit,</li>
    <li>Face painting</li>
    <li>Vintage cars on display</li>
  </ul>
  <ul class="activities activities--right">
    <li>Music</li>
    <li>Refreshments</li>
    <li>50s hairstyles</li>
  </ul>

  <p class="when">
    <span class="when__label">Date:</span> 19th &amp; 20th July<br>
    <span class="when__label">From :</span> 11:00am onwards
  </p>

  <footer class="contact">
    27 HARBOUR VIEW RD, KELSTON<br>
    PH: 53 418....<br>
    MOBILE: 0412555018
  </footer>

  <svg class="decor decor--bottom-left" width="320" height="420" viewBox="0 0 320 420" aria-hidden="true">
    <circle cx="150" cy="110" r="96" fill="var(--yellow)"/>
    <circle cx="125" cy="100" r="78" fill="var(--red)"/>
    <circle cx="110" cy="75" r="52" fill="var(--yellow)"/>
    <circle cx="40" cy="180" r="85" fill="var(--red)"/>
    <circle cx="180" cy="290" r="120" fill="var(--yellow)"/>
    <circle cx="165" cy="300" r="104" fill="var(--white)"/>
    <circle cx="160" cy="308" r="96" fill="var(--red)"/>
    <circle cx="20" cy="330" r="90" fill="var(--yellow)"/>
    <circle cx="30" cy="345" r="72" fill="var(--red)"/>
  </svg>
</main>
</body>
</html>
```